We need a flyer where we promote a workshop to our members of the jewish community www.qvb-gemeinde.example . The workshop is calles "guidance in ten seasons presented by QVB. We would like to see a flyer with the below text is used and also some pictures (attached). The flyer should come over as cool, fresh, innovative for a younger crowd so called young professionals (age 28-35).
TITLE.
"Guidance in Ten Seasons.
SUBTITLE.
Your systematic self-coaching roadmap to power and impact—and your future.”
TEXT.
Dr. Martin K. Halvorsen is the CEO Emeritus of Alpine Advisory Partners—he made an exit in 2013. He is the award-winning author of 8 books, including "Plan-Into-Motion," "Speak or Falter" and "The Cantor and the Chairman.”
For the past 20 years he has taught leadership at Harwick University in New York and at BKU (Lindenberg University) to prepare future CEOs and other leaders in business, government , nonprofits and the military.
Now, in a process exclusively designed for QVB’s next generation of emerging leaders, Martin unpacks his leadership secrets in 3 action-packed labs—reduced to the max:
Lab 1. Guidance in Ten Seasons: The Summit Guide Triangle®. Self-Assessment. Self-Leadership: “The Lantern.” 5-Year Vision. 100-Day Catalytic Project.
Lab 2. Leading Through Language. Relationship: Building Trust. Plan-Into-Motion. Cockpit.
Lab 3. Debrief and Scale-Up. Sustainability. Action Tools.
Do you want to build your own future and a life you love? Do you want to jump-start that future and life over 100 days while learning a toolbox of leadership skills, networking with like-minded people—and even get some pizza? Then join us.
Target Market(s)
young professionals age 28-35

```html
<!DOCTYPE html>
<html lang="en">
<head>
<meta charset="utf-8">
<title>Guidance in Ten Seasons – Workshop Flyer</title>
<link rel="stylesheet" href="https://fonts.googleapis.com/css2?family=Anton&family=Barlow+Condensed:wght@700&family=Oswald:wght@300&family=Rubik:wght@400;500;600&display=swap">
<style>
  :root{
    --orange:#e8401f;
    --teal:#12b5a0;
    --navy:#0a0f2a;
    --ink:#1f1f24;
    --paper:#f5f5f6;
    --white:#ffffff;
    --logo-grey:#4a4a4c;
    --title-shadow:#0d0d12;
  }
  html,body{margin:0;padding:0;width:990px;height:1200px;overflow:hidden;background:var(--white);}
  .flyer{position:relative;width:990px;height:1200px;overflow:hidden;background:var(--paper);font-family:"Rubik",sans-serif;}
  .hero-photo{position:absolute;left:0;top:0;width:990px;height:640px;
    background:
      radial-gradient(ellipse at 12% 20%, #8a0d12 0%, rgba(138,13,18,0) 38%),
      radial-gradient(ellipse at 85% 25%, #33406a 0%, rgba(51,64,106,0) 35%),
      radial-gradient(ellipse at 50% 85%, #1d3f9a 0%, rgba(29,63,154,0) 60%),
      linear-gradient(180deg,#070915 0%,#0b1437 60%,#13286b 100%);}
  .title{position:absolute;left:0;top:0;width:990px;height:420px;}
  .title .line-light{font-family:"Oswald",sans-serif;font-weight:300;}
  .title .line-heavy{font-family:"Anton",sans-serif;}
  .title .shadow{fill:var(--title-shadow);opacity:.75;}
  .subtitle{position:absolute;left:100px;top:445px;width:790px;margin:0;text-align:center;
    font-family:"Barlow Condensed",sans-serif;font-weight:700;font-size:34px;line-height:48px;
    text-transform:uppercase;color:var(--teal);}
  .panel-shape{position:absolute;left:0;top:577px;width:990px;height:390px;}
  .bio{position:absolute;left:65px;top:628px;width:420px;}
  .bio p{margin:0 0 22px;padding-left:19px;border-left:3px solid var(--white);
    color:var(--white);font-size:13.6px;line-height:19px;text-align:justify;}
  .bio strong{font-weight:600;}
  .menorah{position:absolute;left:752px;top:712px;width:132px;height:150px;
    background:linear-gradient(180deg,#f7e3b0 0%,#e9a93a 100%);opacity:.85;border-radius:6px;}
  .portrait{position:absolute;left:505px;top:580px;width:372px;height:380px;
    border-radius:160px 160px 0 0;
    background:linear-gradient(180deg,#c99a7e 0%,#8a8b8f 40%,#4b4d52 100%);}
  .org-badge{position:absolute;left:744px;top:560px;width:176px;height:176px;border-radius:50%;
    background:var(--logo-grey);display:flex;align-items:center;justify-content:center;}
  .org-badge span{font-weight:600;font-size:54px;color:var(--white);letter-spacing:1px;}
  .divider{position:absolute;left:0;top:957px;width:990px;height:4px;background:var(--teal);}
  .labs{position:absolute;left:65px;top:1000px;width:450px;}
  .labs p{margin:0 0 14px;padding-left:19px;border-left:3px solid var(--teal);
    color:var(--ink);font-size:13.6px;line-height:19px;text-align:justify;}
  .labs .lab-no{color:var(--orange);font-weight:500;}
  .invite{position:absolute;left:553px;top:1000px;width:376px;margin:0;padding-left:28px;
    border-left:3px solid var(--teal);box-sizing:border-box;
    color:var(--ink);font-size:13.6px;line-height:19px;text-align:justify;}
  .url-shape{position:absolute;left:0;top:1128px;width:990px;height:72px;}
  .url{position:absolute;left:708px;top:1150px;width:282px;text-align:center;white-space:nowrap;
    color:var(--white);font-weight:600;font-size:18px;letter-spacing:0.3px;}
</style>
</head>
<body>
<main class="flyer">
  <div class="hero-photo" role="img" aria-label="Blurred photo of a conference audience facing a lit stage with a speaker on screen"></div>

  <svg class="title" viewBox="0 0 990 420" aria-label="Guidance in Ten Seasons">
    <defs>
      <linearGradient id="silver" x1="0" y1="0" x2="0" y2="1">
        <stop offset="0" stop-color="#ffffff"/>
        <stop offset="0.55" stop-color="#e4e4e6"/>
        <stop offset="1" stop-color="#9c9ca2"/>
      </linearGradient>
    </defs>
    <g class="line-light" font-size="140">
      <text class="shadow" x="124" y="208" textLength="595" lengthAdjust="spacingAndGlyphs">GUIDANCE</text>
      <text class="shadow" x="764" y="208" textLength="110" lengthAdjust="spacingAndGlyphs">IN</text>
      <text x="120" y="205" textLength="595" lengthAdjust="spacingAndGlyphs" fill="url(#silver)">GUIDANCE</text>
      <text x="760" y="205" textLength="110" lengthAdjust="spacingAndGlyphs" fill="url(#silver)">IN</text>
    </g>
    <g class="line-heavy" font-size="205">
      <text class="shadow" x="124" y="398" textLength="240" lengthAdjust="spacingAndGlyphs">TEN</text>
      <text class="shadow" x="409" y="398" textLength="465" lengthAdjust="spacingAndGlyphs">SEASONS</text>
      <text x="120" y="395" textLength="240" lengthAdjust="spacingAndGlyphs" fill="url(#silver)">TEN</text>
      <text x="405" y="395" textLength="465" lengthAdjust="spacingAndGlyphs" fill="url(#silver)">SEASONS</text>
    </g>
  </svg>

  <p class="subtitle">Your systematic self-coaching roadmap to power and impact—and your future.</p>

  <svg class="panel-shape" viewBox="0 0 990 390" aria-hidden="true">
    <polygon points="0,0 494,0 542,61 990,61 990,390 0,390" fill="var(--orange)"/>
    <polygon points="506,11 518,11 556,61 540,61" fill="var(--teal)"/>
  </svg>

  <section class="bio">
    <p><strong>Dr. Martin K. Halvorsen</strong> is the CEO Emeritus of Alpine Advisory Partners—he made an exit in 2013. He is the award-winning author of 8 books, including "Plan-Into-Motion," "Speak or Falter" and "The Cantor and the Chairman."</p>
    <p>For the past 20 years he has taught leadership at Harwick University in New York and at BKU (Lindenberg University) to prepare future CEOs and other leaders in business, government, nonprofits and the military.</p>
    <p>Now, in a process exclusively designed for QVB’s next generation of emerging leaders, Martin unpacks his leadership secrets in 3 action-packed labs—reduced to the max:</p>
  </section>

  <div class="menorah" role="img" aria-label="Illustration of a golden menorah with lit candles"></div>
  <div class="portrait" role="img" aria-label="Photo of the presenter in a grey suit with arms crossed"></div>
  <div class="org-badge"><span>QVB</span></div>

  <div class="divider"></div>

  <section class="labs">
    <p><span class="lab-no">Lab 1.</span> Guidance in Ten Seasons: The Summit Guide Triangle®. Self-Assessment. Self-Leadership: “The Lantern.” 5-Year Vision. 100-Day Catalytic Project.</p>
    <p><span class="lab-no">Lab 2.</span> Leading Through Language. Relationship: Building Trust. Plan-Into-Motion. Cockpit.</p>
    <p><span class="lab-no">Lab 3.</span> Debrief and Scale-Up. Sustainability. Action Tools.</p>
  </section>

  <p class="invite">Do you want to build your own future and a life you love? Do you want to jump-start that future and life over 100 days while learning a toolbox of leadership skills, networking with like-minded people—and even get some pizza? Then join us.</p>

  <svg class="url-shape" viewBox="0 0 990 72" aria-hidden="true">
    <polygon points="729,2 990,2 990,72 688,72" fill="var(--orange)"/>
    <polygon points="713,12 725,12 681,65 669,65" fill="var(--teal)"/>
    <rect x="0" y="65" width="990" height="7" fill="var(--orange)"/>
  </svg>
  <div class="url">www.qvb-gemeinde.example</div>
</main>
</body>
</html>
```